Speisekarte Heuriger
Zielgruppe
Wir sind ein Gastronomielokal im Burgenland. Ein Heuriger ist ein traditionelles Lokal in dem hauptsächlich kalte und einfache warme Speisen verabreicht werden. (Brote, kaltes und warmes gebratenes Fleisch, gemischte Teller, Strudl usw.) Aber ein großer Schwerpunkt liegt dabei auch immer auf den eigenen Weinen.
Aufgabenstellung
Da ein Heuriger aus dem Weinbau und somit Landwirtschaft kommt bevorzuge ich eher ein schlichtes traditionelles Design. Ein grüner Farbbereich ist vielleicht das Beste. (nicht stechend grün. eher hell) (Vielleicht im Internet nach Speisekarte Heuriger/Buschenschank suchen)
Ich benötige eine Vorlage für die Speisekarte in Indesign am besten erstellt mit dem drukwelle.at plugin damit die Größen passen.
Speisekarte mit Umschlag 8 Innenseiten mit 4seitigem Umschlag haben.
In A5 hoch
CMYK-Farbmodell
Klammerheftung
Umschlag:
Vorderseite natürlich mit "Speisekarte" drauf mit Logo, Und evtl der Name: "Heuriger Familie Pelkinger" usw.
die vordere Innenseite kann leer sein. Evtl auch gesamte Anschrift hier rein. Oder auch auf die Rückseite. Das ist freigestellt.
Auf der hinteren Innenseite muss die Allergenverordnung mit den Allergenen und dazugehörigen Buchstaben vorhanden sein! (Achtung für Österreich! Gibt genug Beispielbilder im Internet)
Auf der Rückseite hinten sollte stehen: "Wir bedanken uns für Ihren Besuch und freuen uns darauf, Sie bald wieder bei uns begrüßen zu dürfen!
Familie Pelkinger" (Natürlich nicht in einer Wurst)
Innenseiten: (Text schreibe ich selber. Aber vielleicht ein paar Beispiele für Schriftart und Größe/Farbe)
Erste Seite (rechts): Getränke
Zweite Seite: Kalte Speisen
Dritte Seite: Brote
Vierte Seite: Warme Speisen
Fünfte Seite: Beilagen/Salate
Sechste Seite: Für unsere kleinen Gäste/ Strudel
Siebente Seite: Weißwein
Achte Seite: Rotwein
Die Seitenbelegung ist nur als Info gedacht. Ich habe leider keine schönen Fotos von den Speisen gemacht und will auch keine fremden Speisen in meiner Karte sehen. Also keine Speisebilder. (Mit Ausnahme von Weintrauben vielleicht. Bezug zum Weinbau usw.)
Anbei habe ich die Logos von unseren Etiketten. Man kann das P auch alleine ohne dem Namen darunt..

```html
<!DOCTYPE html>
<html lang="de">
<head>
<meta charset="utf-8">
<title>Speisekarte – Heuriger Familie Pelkinger</title>
<link href="https://fonts.googleapis.com/css2?family=Lato:wght@400;700&display=swap" rel="stylesheet">
<style>
  :root {
    --paper: #f3f3e6;
    --green: #6cbf2a;
    --ink: #1f1f1f;
    --rule: #d4d4c8;
  }
  * { box-sizing: border-box; margin: 0; padding: 0; }
  html, body { width: 1200px; height: 854px; overflow: hidden; background: #fff; }
  .spread {
    position: relative; width: 1200px; height: 854px;
    background: var(--paper);
    font-family: "Lato", Arial, sans-serif; color: var(--ink);
    border: 1px solid var(--rule);
  }
  .page { position: absolute; top: 0; width: 600px; height: 854px; }
  .page--left { left: 0; }
  .page--right { left: 600px; }

  .brand {
    position: absolute; top: 62px; left: 0; width: 100%;
    display: flex; justify-content: center; align-items: center; gap: 10px;
  }
  .brand__square { width: 14px; height: 14px; background: var(--green); }
  .brand__name {
    font-size: 22px; font-weight: 400; letter-spacing: 4px;
    text-transform: uppercase; color: var(--green);
  }

  .section-title {
    position: absolute; display: flex; justify-content: center; align-items: center; gap: 10px;
    border-bottom: 1.5px solid var(--green); padding-bottom: 6px;
    font-size: 19px; font-weight: 400; letter-spacing: 1px; text-transform: uppercase;
  }
  .section-title svg { display: block; }

  .item {
    position: absolute; display: flex; justify-content: space-between; align-items: flex-end;
    font-size: 13.5px; line-height: 19px;
  }
  .page--left .item { left: 76px; width: 440px; }
  .page--right .item { left: 81px; width: 438px; }
  .item__name { font-weight: 700; }
  .item__desc { font-weight: 400; }
  .item__price { font-weight: 700; white-space: nowrap; padding-left: 16px; }

  .footer { position: absolute; top: 748px; left: 187px; width: 219px; text-align: center; }
  .footer__name {
    font-size: 10.5px; letter-spacing: 0.4px; text-transform: uppercase; color: var(--green);
    border-bottom: 1px solid var(--green); padding-bottom: 6px;
  }
  .footer__icons { display: flex; justify-content: center; gap: 11px; margin-top: 12px; }
  .footer__icon { width: 45px; height: 45px; background: var(--green); display: flex; align-items: center; justify-content: center; }
</style>
</head>
<body>
<div class="spread">

  <section class="page page--left">
    <div class="brand"><span class="brand__square"></span><span class="brand__name">Pelkinger</span></div>

    <h2 class="section-title" style="top:168px; left:169px; width:262px;">
      <svg width="66" height="12" viewBox="0 0 66 12"><rect x="0" y="5" width="40" height="2.4" rx="1.2" fill="#6cbf2a"/><ellipse cx="54" cy="6" rx="12" ry="5.5" fill="#6cbf2a"/></svg>
      Warme Speisen
    </h2>

    <div class="item" style="top:245px;"><span><span class="item__name">Heurigenteller |</span> <span class="item__desc">(Surbraten, Schweinsbraten,<br>Kümmelbraten, ein Stück Blunze, Sauerkraut und Knödel)</span></span><span class="item__price">€ 7.00</span></div>
    <div class="item" style="top:309px;"><span><span class="item__name">Surbraten |</span> <span class="item__desc">mager</span></span><span class="item__price">€ 5.00</span></div>
    <div class="item" style="top:355px;"><span><span class="item__name">Schweinsbraten |</span> <span class="item__desc">vom Schopf</span></span><span class="item__price">€ 5.00</span></div>
    <div class="item" style="top:400px;"><span><span class="item__name">Kümmelbraten |</span> <span class="item__desc">saftig gebraten</span></span><span class="item__price">€ 5.00</span></div>
    <div class="item" style="top:445px;"><span><span class="item__name">Fleischlaibchen |</span> <span class="item__desc">2 Stück, nach Art des Hauses</span></span><span class="item__price">€ 4.00</span></div>
    <div class="item" style="top:490px;"><span><span class="item__name">Gegrillte Blunze |</span> <span class="item__desc">mit Senf und Kren</span></span><span class="item__price">€ 4.00</span></div>

    <footer class="footer">
      <p class="footer__name">Heuriger Familie Pelkinger e.U.</p>
      <div class="footer__icons">
        <span class="footer__icon"><svg width="22" height="34" viewBox="0 0 22 34"><path d="M2 1h18c0 10-3 15-8 16v12h5v3H5v-3h5V17C5 16 2 11 2 1z" fill="#fff"/></svg></span>
        <span class="footer__icon"><svg width="18" height="36" viewBox="0 0 18 36"><path d="M1 1h2v10h2V1h2v10h2V1h2v10h2V1h2v11c0 3-2 5-5 5v18H8V17c-3 0-6-2-6-5z" fill="#fff" transform="translate(1 0) scale(0.9 1)"/></svg></span>
        <span class="footer__icon"><svg width="14" height="36" viewBox="0 0 14 36"><path d="M9 1c3 4 4 10 3 18H9v15H5V19C4 10 5 4 9 1z" fill="#fff"/></svg></span>
      </div>
    </footer>
  </section>

  <section class="page page--right">
    <div class="brand"><span class="brand__square"></span><span class="brand__name">Pelkinger</span></div>

    <h2 class="section-title" style="top:168px; left:131px; width:327px;">
      <svg width="70" height="12" viewBox="0 0 70 12"><rect x="0" y="5" width="44" height="2.4" rx="1.2" fill="#6cbf2a"/><path d="M44 3h14v6H44z" fill="#6cbf2a"/><rect x="56" y="2" width="14" height="1.5" fill="#6cbf2a"/><rect x="56" y="5.2" width="14" height="1.5" fill="#6cbf2a"/><rect x="56" y="8.5" width="14" height="1.5" fill="#6cbf2a"/></svg>
      Beilagen
    </h2>

    <div class="item" style="top:246px;"><span><span class="item__name">Kartoffelsalat |</span> <span class="item__desc">(hausgemacht)</span></span><span class="item__price">€ 1.50</span></div>
    <div class="item" style="top:291px;"><span><span class="item__name">Krautsalat</span></span><span class="item__price">€ 1.50</span></div>
    <div class="item" style="top:337px;"><span><span class="item__name">Sauerkraut</span></span><span class="item__price">€ 1.50</span></div>
    <div class="item" style="top:382px;"><span><span class="item__name">Semmelknödel</span></span><span class="item__price">€ 1.50</span></div>

    <h2 class="section-title" style="top:432px; left:131px; width:327px;">
      <svg width="70" height="12" viewBox="0 0 70 12"><rect x="0" y="5" width="44" height="2.4" rx="1.2" fill="#6cbf2a"/><path d="M44 3h14v6H44z" fill="#6cbf2a"/><rect x="56" y="2" width="14" height="1.5" fill="#6cbf2a"/><rect x="56" y="5.2" width="14" height="1.5" fill="#6cbf2a"/><rect x="56" y="8.5" width="14" height="1.5" fill="#6cbf2a"/></svg>
      Salate
    </h2>

    <div class="item" style="top:499px;"><span><span class="item__name">Wurstsalat |</span> <span class="item__desc">(mit Käse, Paprika und Joghurtdressing)</span></span><span class="item__price">€ 4.00</span></div>
    <div class="item" style="top:544px;"><span><span class="item__name">Nudelsalat |</span> <span class="item__desc">(mit Schinken, Tomaten,<br>Paprika und American Dressing)</span></span><span class="item__price">€ 4.00</span></div>
    <div class="item" style="top:608px;"><span><span class="item__name">Salatteller |</span> <span class="item__desc">(mit grünem Salat, Krautsalat, Fisolensalat,<br>Karottensalat, Tomaten, Schinken und Ei) - nur im Sommer</span></span><span class="item__price">€ 5.00</span></div>
    <div class="item" style="top:672px;"><span><span class="item__name">Bunter Salat |</span> <span class="item__desc">(mit Blattsalat, Tomaten, Gurke, Mais,<br>Rohschinken und Ei) - nur im Sommer</span></span><span class="item__price">€ 5.00</span></div>

    <footer class="footer" style="left:191px;">
      <p class="footer__name">Heuriger Familie Pelkinger e.U.</p>
      <div class="footer__icons">
        <span class="footer__icon"><svg width="22" height="34" viewBox="0 0 22 34"><path d="M2 1h18c0 10-3 15-8 16v12h5v3H5v-3h5V17C5 16 2 11 2 1z" fill="#fff"/></svg></span>
        <span class="footer__icon"><svg width="18" height="36" viewBox="0 0 18 36"><path d="M1 1h2v10h2V1h2v10h2V1h2v10h2V1h2v11c0 3-2 5-5 5v18H8V17c-3 0-6-2-6-5z" fill="#fff" transform="translate(1 0) scale(0.9 1)"/></svg></span>
        <span class="footer__icon"><svg width="14" height="36" viewBox="0 0 14 36"><path d="M9 1c3 4 4 10 3 18H9v15H5V19C4 10 5 4 9 1z" fill="#fff"/></svg></span>
      </div>
    </footer>
  </section>

</div>
</body>
</html>
```